Quick Order Banner Design

We want to build a banner that will sit in the middle of the page that will replace our current quick order banner that we don't like. See https://www.snapvellum.com/image/48230917?key=3f91ac2de7b4c8e05a6d1f29b73e4c0a

Text:
Quick Order is a fast and easy way to fill your cart with items when you know exactly what you want to purchase.

Design ideas:

Use foto Noto Sans. Color codes can be of #00539E, FDBC38, #6AC07A

We don't want a computer screen in banner nor a person. You can look at our competitors below for ideas.

i don't like the design here https://tovirapartsdepot.com/blog/post/order-parts-fast-with-our-new-quick-order-feature but the concept is cool as it shows where to access it.. but i want other ideas too.

Our staging server is plimdex4.com

Our competitors:
https://www.halvorsupplyco.com/
https://www.lumbrix.com/
https://www.vosko.com/
https://www.quelt.com/index.html

Target Market(s)

B2B, Contractors who buy our products

Industry/Entity Type

hvac

Requirements
Should not have
• people photos or computer or computer screens.

```html
<!DOCTYPE html>
<html lang="en">
<head>
<meta charset="utf-8">
<title>Quick Order Banner</title>
<link href="https://fonts.googleapis.com/css2?family=Noto+Sans:wght@600;700&display=swap" rel="stylesheet">
<style>
  :root {
    --stage: #606060;
    --brand-blue: #00539E;
    --deep-blue: #1B3A8E;
    --stripe-blue: #2A6CC0;
    --accent-yellow: #FDBC38;
    --accent-green: #6AC07A;
    --ink-dark: #1E2A33;
    --white: #FFFFFF;
    --photo-navy: #2A3548;
    --photo-amber: #C9762E;
  }
  html, body {
    margin: 0;
    padding: 0;
    width: 1200px;
    height: 508px;
    overflow: hidden;
    background: var(--stage);
  }
  .banner {
    position: absolute;
    left: 38px;
    top: 88px;
    width: 1127px;
    height: 322px;
    overflow: hidden;
    font-family: "Noto Sans", Arial, sans-serif;
  }
  .banner-art {
    position: absolute;
    inset: 0;
    width: 100%;
    height: 100%;
  }
  .banner-copy {
    position: absolute;
    left: 38px;
    top: 36px;
    color: var(--white);
  }
  .headline {
    margin: 0;
    font-size: 64px;
    font-weight: 700;
    line-height: 1;
    color: var(--accent-yellow);
    letter-spacing: 0.5px;
  }
  .lead {
    margin: 14px 0 0;
    font-size: 25px;
    font-weight: 700;
    line-height: 37px;
    width: 560px;
  }
  .site-tag {
    position: absolute;
    left: 34px;
    top: 245px;
    width: 247px;
    height: 36px;
    background: var(--accent-green);
    color: var(--ink-dark);
    font-size: 20px;
    font-weight: 600;
    line-height: 36px;
    text-align: center;
  }
</style>
</head>
<body>
  <section class="banner">
    <svg class="banner-art" viewBox="0 0 1127 322" preserveAspectRatio="none" aria-hidden="true">
      <defs>
        <linearGradient id="blue-field" x1="0" y1="0" x2="1" y2="1">
          <stop offset="0" stop-color="var(--deep-blue)"/>
          <stop offset="0.6" stop-color="var(--brand-blue)"/>
          <stop offset="1" stop-color="var(--deep-blue)"/>
        </linearGradient>
        <linearGradient id="photo-tone" x1="0" y1="0" x2="1" y2="1">
          <stop offset="0" stop-color="var(--photo-navy)"/>
          <stop offset="0.55" stop-color="var(--photo-amber)"/>
          <stop offset="1" stop-color="var(--photo-navy)"/>
        </linearGradient>
      </defs>
      <rect class="field" width="1127" height="322" fill="url(#blue-field)"/>
      <polygon class="stripe" points="130,0 330,0 60,322 0,322 0,150" fill="var(--stripe-blue)" opacity="0.35"/>
      <polygon class="stripe" points="360,0 540,0 300,322 120,322" fill="var(--stripe-blue)" opacity="0.3"/>
      <polygon class="stripe" points="600,0 760,0 490,322 380,322" fill="var(--stripe-blue)" opacity="0.35"/>
      <polygon class="accent-band" points="477,322 562,322 800,0 790,0" fill="var(--accent-yellow)"/>
      <polygon class="photo-area" points="800,0 1127,0 1127,322 562,322" fill="url(#photo-tone)" role="img" aria-label="Photo of a cardboard shipping box on flaming wheels racing forward"/>
    </svg>

    <div class="banner-copy">
      <h1 class="headline">Quick Order</h1>
      <p class="lead">is a fast and easy way to fill your cart with items when you know exactly what you want to purchase.</p>
    </div>
    <div class="site-tag">plimdex4.com</div>
  </section>
</body>
</html>
```